Global Voltaris Power Technology Company needs initial Web Design

We need a web design for new Voltaris Power Technology company. The company has developed innovative technology and needs a website to reflect this branding. Whilst this assignment will represent the initial site we are seeking an ongoing relationship to allow the website to be developed as the business develops. The logo design and initial artwork has been done and needs to incorporated in the design.

Target Market(s)

Business decision makers and power generation companies
Initially two target markets
1. Commercial users like construction companies or industrial businesses like mining that currently utilize Diesel generators to create power
2. Electrical power suppliers that currently use diesel generators in regional and remote to supply remote communities like outback Australia or pacific islands like Fuji etc
The purpose initially is to showcase/ educate customers about the product but we ideally would like to capture email addressees as part of this process.

The product information has been limited at this stage as we are currently finalizing IP registrations.

The main competitors are
1 Solar energy products but these only generate power when the sun is shinning and needs to be stored which battery technology is expensive and will only last up to 3 days at most
2 Wind energy would the same as as solar
3 Diesel generators run continually but are expensive to operate. Our product would be approximately 1/2 the operating cost of this energy source. There is no reliance on fuel sources so the user doesn't need to store fuel, worry about running out or fluctuations in fuel pricing. Diesel generators are very noisy and not environmentally friendly.

Industry/Entity Type

Solar Energy

Coding

Coded - Design and coding required

Number of Pages Required

4 page

Font styles to use
Sans Serif

Colors
acd036
33a6d7
ffffff

Requirements
Must have
• This version is intended as an initial basic 4 page website only.
• It should be built on the basis that it can be expanded after the products are formally launched into the market. A separate assignment will be allocated to the successful initial website designer to create a more elaborate site with a budget to match. The format and content for the initial site is outlined in the attached word document (File 1) The remaining files contain the logo and existing artwork and associated colours. The site should have the ability to view on smart phones and tablets.

```html
<!DOCTYPE html>
<html lang="en">
<head>
<meta charset="utf-8">
<title>Voltaris Power — Perpetua</title>
<link rel="stylesheet" href="https://fonts.googleapis.com/css2?family=Arimo:wght@400;700&family=Open+Sans:wght@400;600&family=Roboto+Condensed:wght@700&display=swap">
<style>
  :root {
    --green: #acd036;
    --blue: #33a6d7;
    --white: #ffffff;
    --nav-blue: #1f86c2;
    --ink: #111111;
    --slate: #2b3e4a;
    --hero-text: #1f3440;
    --list-text: #2f6178;
    --band-grey: #f3f3f3;
    --partner-ink: #3f4a24;
  }
  * { margin: 0; padding: 0; box-sizing: border-box; }
  html, body { width: 882px; height: 1200px; overflow: hidden; background: var(--white); }
  body { font-family: "Arimo", Arial, sans-serif; color: var(--ink); }
  .page { position: relative; width: 882px; height: 1200px; overflow: hidden; }

  /* Header */
  .site-header {
    position: absolute; left: 0; top: 0; width: 882px; height: 103px;
    background: linear-gradient(180deg, #c9e6f2 0, #c9e6f2 6px, #e4f2f8 7px, #d8edf6 100%);
  }
  .brand { position: absolute; left: 122px; top: 18px; display: flex; align-items: center; gap: 14px; }
  .brand-mark { width: 60px; height: 60px; border-radius: 50%; background: var(--blue); }
  .brand-name {
    font-family: "Open Sans", Arial, sans-serif; font-weight: 600; font-size: 22px;
    color: var(--green); letter-spacing: 1px; line-height: 1;
  }
  .main-nav { position: absolute; top: 46px; left: 0; width: 882px; height: 20px; }
  .main-nav a {
    position: absolute; font-family: "Open Sans", Arial, sans-serif; font-weight: 600;
    font-size: 13.5px; color: var(--ink); text-decoration: none; letter-spacing: -0.2px;
  }
  .main-nav a.is-current { color: var(--nav-blue); }

  /* Hero */
  .hero {
    position: absolute; left: 0; top: 103px; width: 882px; height: 400px;
    background: radial-gradient(ellipse 70% 60% at 45% 25%, #b8def0 0%, #8ccbe7 55%, #5fb4dc 100%);
  }
  .hero-title {
    position: absolute; left: 141px; top: 53px; font-weight: 700; font-size: 24px;
    letter-spacing: 2px; color: var(--slate);
  }
  .hero-intro {
    position: absolute; left: 141px; top: 128px; width: 315px; font-size: 13px;
    line-height: 15.5px; letter-spacing: 0.6px; text-align: justify; text-align-last: left;
    color: var(--hero-text);
  }
  .hero-benefits {
    position: absolute; left: 155px; top: 237px; list-style: none; font-size: 13px;
    line-height: 15.5px; letter-spacing: 0.6px; color: var(--list-text);
  }
  .hero-benefits li::before { content: "•"; display: inline-block; width: 20px; font-size: 9px; vertical-align: 1px; }
  .product-visual {
    position: absolute; left: 505px; top: 92px; width: 242px; height: 265px;
    border-radius: 4px;
    background: linear-gradient(135deg, #f4f6f7 0%, #e3e8ea 45%, #2fa3d8 46%, #1f8fc6 100%);
  }

  /* Why band */
  .why-band {
    position: absolute; left: 0; top: 503px; width: 882px; height: 90px;
    background: var(--band-grey); display: flex; align-items: center; justify-content: center;
  }
  .why-band h2 {
    font-family: "Roboto Condensed", "Arial Narrow", sans-serif; font-weight: 700;
    font-size: 23px; color: var(--ink); letter-spacing: -0.2px;
  }

  /* Features */
  .feature { position: absolute; width: 252px; text-align: center; }
  .feature-icon { display: block; width: 62px; height: 62px; margin: 0 auto 10px; }
  .feature p { font-size: 12px; line-height: 14.2px; letter-spacing: 0.5px; color: var(--ink); }
  .feature--efficiency { left: 163px; top: 634px; }
  .feature--cycle { left: 464px; top: 634px; }
  .feature--modular { left: 163px; top: 835px; }
  .feature--support { left: 464px; top: 835px; }

  /* Partners */
  .partners {
    position: absolute; left: 0; top: 1033px; width: 882px; height: 167px; background: var(--green);
  }
  .partners h2 {
    position: absolute; top: 13px; width: 100%; text-align: center;
    font-family: "Arimo", Arial, sans-serif; font-weight: 400; font-size: 25px; color: #1d2a12;
  }
  .partner-badge { position: absolute; background: var(--partner-ink); }
  .badge-one { left: 124px; top: 83px; width: 106px; height: 26px; border-radius: 13px; }
  .badge-two { left: 259px; top: 80px; width: 104px; height: 32px; border-radius: 50%; }
  .badge-three { left: 391px; top: 82px; width: 100px; height: 28px; border-radius: 4px; }
  .badge-four { left: 532px; top: 84px; width: 74px; height: 24px; border-radius: 4px; }
  .badge-five { left: 650px; top: 86px; width: 106px; height: 20px; border-radius: 2px; }
</style>
</head>
<body>
<div class="page">

  <header class="site-header">
    <div class="brand">
      <span class="brand-mark"></span>
      <span class="brand-name">VOLTARIS POWER</span>
    </div>
    <nav class="main-nav">
      <a class="is-current" href="#" style="left:470px">HOME</a>
      <a href="#" style="left:528px">CONTACT US</a>
      <a href="#" style="left:625px">PRODUCT</a>
      <a href="#" style="left:722px">TEAM</a>
    </nav>
  </header>

  <section class="hero">
    <h1 class="hero-title">PERPETUA</h1>
    <p class="hero-intro">Voltaris Power has developed patented electric power generation technology that revolutionises the way the world will think about power generation for generations to come</p>
    <ul class="hero-benefits">
      <li>24 hour a day power</li>
      <li>No fuel sources</li>
      <li>Environmentally friendly</li>
      <li>Scalable and relocatable</li>
      <li>Quick and easy installation</li>
      <li>Full maintenance support</li>
      <li>24 hour monitoring</li>
      <li>20 year &nbsp;warranty</li>
    </ul>
    <div class="product-visual" role="img" aria-label="Product photo of the Perpetua generator unit, a white and blue cabinet with an open control panel"></div>
  </section>

  <section class="why-band">
    <h2>Why choose Voltaris Power?</h2>
  </section>

  <div class="feature feature--efficiency">
    <svg class="feature-icon" viewBox="0 0 62 62" aria-hidden="true">
      <circle cx="31" cy="31" r="31" fill="#33a6d7"/>
      <path d="M17 16 V45 H46" fill="none" stroke="#fff" stroke-width="2"/>
      <path d="M21 41 C27 41 27 25 32 25 L43 23" fill="none" stroke="#fff" stroke-width="2"/>
    </svg>
    <p>The advanced generator technology has been designed in a way that there are minimal energy losses. The generator, coupled with the intelligent mechanical and electronic multipliers, allows the system to produce very high input to output ratios resulting in ratios of 1 to 100 outputs.</p>
  </div>

  <div class="feature feature--cycle">
    <svg class="feature-icon" viewBox="0 0 62 62" aria-hidden="true">
      <circle cx="31" cy="31" r="31" fill="#33a6d7"/>
      <path d="M18 28 A13 13 0 0 1 42 24" fill="none" stroke="#fff" stroke-width="3"/>
      <path d="M44 34 A13 13 0 0 1 20 38" fill="none" stroke="#fff" stroke-width="3"/>
      <path d="M45 17 L44 27 L36 23 Z" fill="#fff"/>
      <path d="M17 45 L18 35 L26 39 Z" fill="#fff"/>
    </svg>
    <p>The advanced generator technology has been designed in a way that there are minimal energy losses. The generator, coupled with the intelligent mechanical and electronic multipliers, allows the system to produce very high input to output ratios resulting in ratios of 1 to 100 outputs.</p>
  </div>

  <div class="feature feature--modular">
    <svg class="feature-icon" viewBox="0 0 62 62" aria-hidden="true">
      <circle cx="31" cy="31" r="31" fill="#33a6d7"/>
      <g fill="none" stroke="#fff" stroke-width="2">
        <path d="M20 26 V20 H26 M20 20 L27 27"/>
        <path d="M42 26 V20 H36 M42 20 L35 27"/>
        <path d="M20 36 V42 H26 M20 42 L27 35"/>
        <path d="M42 36 V42 H36 M42 42 L35 35"/>
      </g>
    </svg>
    <p>The Units are designed for quick and easy installation allowing them to be scalable and relocatable. The Units are designed to operate in modular fashion allowing for power scaling and redundancy to supply 24 hour power to a grid or private power network.</p>
  </div>

  <div class="feature feature--support">
    <svg class="feature-icon" viewBox="0 0 62 62" aria-hidden="true">
      <circle cx="31" cy="31" r="31" fill="#33a6d7"/>
      <path d="M31 14 C36 18 41 19 46 19 C46 34 41 43 31 49 C21 43 16 34 16 19 C21 19 26 18 31 14 Z" fill="none" stroke="#fff" stroke-width="2.5"/>
    </svg>
    <p>To ensure minimum down time, all Units are provided on a fully maintained basis, supported &nbsp;by 24 hour remote monitoring and a 20 year warranty.</p>
  </div>

  <section class="partners">
    <h2>Our Partners</h2>
    <span class="partner-badge badge-one"></span>
    <span class="partner-badge badge-two"></span>
    <span class="partner-badge badge-three"></span>
    <span class="partner-badge badge-four"></span>
    <span class="partner-badge badge-five"></span>
  </section>

</div>
</body>
</html>
```